Playful Website Design Needed Pet Sitting and Dog Walking Business

Need a simple one page Web Design Built on WordPress.
Sections:

About Us
Services Provided
Costs
Contact Us
Intake Form (Questionnaire that goes to email)
See us in Action

Industry/Entity Type

Pet Sitting and Dog Walking

Number of Pages Required

1 page

Font styles to use
Other font styles liked:
• See the Business Card Font and use that.

Colors
EE7325
F08F49
F5BC92
FAE3D3
FDF4ED

Requirements
Must have
• See attached Logo Design, with Font's and Colors Use these as theme guide

```html
<!DOCTYPE html>
<html lang="en">
<head>
<meta charset="utf-8">
<title>Paws Pals Pet Care</title>
<link rel="stylesheet" href="https://fonts.googleapis.com/css2?family=Lobster&family=Baloo+2:wght@400;500;600;700&display=swap">
<style>
:root{
  --orange:#ee7325;
  --orange-mid:#f08f49;
  --peach:#f5bc92;
  --cream:#fae3d3;
  --light:#fdf4ed;
  --page:#fdfaf7;
  --ink:#2b2b2b;
  --muted:#555;
  --yellow:#f6ec12;
  --white:#fff;
}
*{box-sizing:border-box;margin:0;padding:0}
html,body{width:1200px;height:3807px;overflow:hidden}
body{position:relative;background:var(--page);font-family:"Baloo 2",sans-serif;color:var(--ink)}
.abs{position:absolute}
.script{font-family:"Lobster",cursive;font-weight:400}
.btn{position:absolute;display:flex;align-items:center;justify-content:center;background:var(--orange);color:var(--white);border-radius:30px;font-weight:700;font-size:17px;height:58px;width:241px}
.copy{font-size:12.5px;line-height:25px;color:var(--muted)}

/* hero */
.hero{left:0;top:0;width:1200px;height:686px;background:linear-gradient(180deg,#7d8a7a 0%,#a58a5c 40%,#6f7a3b 70%,#4f5a2a 100%)}
.hero-shade{left:0;top:0;width:1200px;height:686px;background:linear-gradient(90deg,rgba(0,0,0,.35),rgba(0,0,0,0) 60%)}
.brand{left:109px;top:30px;width:190px;color:var(--orange);font-size:26px;font-weight:700;line-height:28px;display:flex;align-items:center;gap:10px}
.brand-dot{width:36px;height:36px;border-radius:50%;background:var(--yellow);flex:none}
.nav{right:94px;top:27px;display:flex;align-items:center;gap:32px;color:var(--white);font-size:17px}
.nav-home{width:50px;height:50px;border-radius:50%;background:var(--orange);display:flex;align-items:center;justify-content:center}
.hero-title{left:111px;top:258px;font-size:54px;color:var(--white)}
.hero-text{left:111px;top:335px;width:410px;font-size:13.5px;line-height:28px;color:var(--white)}
.dots{left:559px;top:639px;display:flex;gap:4px}
.dots span{width:13px;height:13px;border-radius:50%;border:2px solid var(--white)}
.dots span.on{border-color:var(--yellow);background:radial-gradient(circle,var(--yellow) 40%,transparent 45%)}

/* about & costs */
.arch{border-radius:220px 220px 4px 4px}
.sec-title{font-size:44px;color:var(--orange)}

/* services */
.band{left:0;top:1410px;width:1200px;height:291px;background:var(--orange)}
.card{top:1567px;width:309px;height:406px;border-radius:28px}
.card-label{top:1990px;width:309px;text-align:center;font-size:22px;color:var(--ink)}

/* badge */
.badge{left:770px;top:2471px;width:205px;height:172px;background:var(--yellow);border-radius:102px 102px 0 0;display:flex;flex-direction:column;align-items:center;justify-content:center;padding-top:20px;color:#222;font-size:28px;line-height:44px;font-weight:500}
.badge small{font-size:13px}

/* contact */
.contact{left:0;top:2764px;width:1200px;height:600px;background:linear-gradient(120deg,#3a2a22 0%,#6a4a3a 45%,#8a3b3b 70%,#3b2d28 100%)}
.contact-shade{left:0;top:2764px;width:1200px;height:600px;background:rgba(0,0,0,.35)}
.field{background:rgba(40,40,40,.55);color:var(--white);font-size:14px;padding:0 18px;display:flex;align-items:center}

/* footer */
.footer{left:0;top:3364px;width:1200px;height:443px;background:var(--orange);color:var(--white)}
.f-head{font-size:17px;font-weight:700;top:3438px}
.f-rule{height:2px;width:30px;background:var(--white);top:3470px}
.f-list{font-size:13px;line-height:26.5px;top:3490px}
.f-small{font-size:11px;font-weight:700;letter-spacing:.3px}
.social{width:48px;height:48px;border-radius:50%;border:1.5px solid var(--white);top:3632px;display:flex;align-items:center;justify-content:center;color:var(--white);font-size:12px;font-weight:600}
</style>
</head>
<body>

<!-- hero -->
<div class="abs hero" role="img" aria-label="Photo of three dogs playing on a grassy field"></div>
<div class="abs hero-shade"></div>
<div class="abs brand"><span class="brand-dot"></span>Paws Pals Pet Care</div>
<nav class="abs nav">
  <span class="nav-home">
    <svg width="26" height="24" viewBox="0 0 26 24" fill="none" stroke="#fff" stroke-width="2"><path d="M2 11 13 2l11 9"/><path d="M5 9v13h16V9"/><path d="M10 22v-7h6v7"/></svg>
  </span>
  <span>About Us</span><span>Services</span><span>Costs</span><span>Contact Us</span>
</nav>
<h1 class="abs hero-title script">Paws Pals Pet Care</h1>
<p class="abs hero-text">Lorem ipsum dolor sit amet, consectetur adipiscing elit, eiusmod tempor incididunt ut labore et dolore magna aliqua. Ut enim ad minim veniam, quis nostrud exercitation</p>
<a class="btn" style="left:111px;top:440px">See us in Action</a>
<div class="abs dots"><span class="on"></span><span></span><span></span><span></span><span></span></div>

<!-- about -->
<div class="abs arch" style="left:114px;top:754px;width:427px;height:529px;background:linear-gradient(180deg,#e6e3de 0%,#d8cfc0 45%,#b9bcb4 100%)" role="img" aria-label="Photo of a golden retriever sitting beside a food bowl"></div>
<h2 class="abs sec-title script" style="left:600px;top:836px">About Us</h2>
<p class="abs copy" style="left:600px;top:912px;width:485px">Lorem ipsum dolor sit amet, consectetur adipiscing elit, sed do eiusmod tempor incididunt ut labore et dolore magna aliqua. Ut enim ad minim veniam, quis nostrud exercitation laboris nisi ut aliquip ex ea commodo consequat. Duis aute irure dolor in reprehenderit in voluptate velit esse cillum dolore eu fugiat nulla pariatur. Excepteur sint occaecat cupidatat non proident, sunt in culpa qui officia deserunt mollit anim id est laborum</p>
<p class="abs copy" style="left:600px;top:1051px;width:485px">Lorem ipsum dolor sit amet, consectetur adipiscing elit, sed do eiusmod tempor incididunt ut labore et dolore magna aliqua. Ut enim ad minim veniam, quis nostrud exercitation laboris nisi ut aliquip ex ea commodo consequat. Duis aute irure dolor in reprehenderit in voluptate velit esse cillum dolore eu fugiat nulla pariatur. Excepteur sint occaecat cupidatat non proident, sunt in culpa qui officia deserunt mollit anim id est laborum</p>
<a class="btn" style="left:600px;top:1206px">Read More</a>

<!-- services -->
<div class="abs band"></div>
<h2 class="abs script" style="left:0;width:1200px;text-align:center;top:1465px;font-size:44px;color:var(--white)">Our Services</h2>
<div class="abs card" style="left:111px;background:linear-gradient(160deg,#dfe3e6,#c9a77a 55%,#8a6a4c)" role="img" aria-label="Photo of puppies eating from metal bowls"></div>
<div class="abs card" style="left:446px;background:linear-gradient(180deg,#6f7d6a,#b8b0a0 45%,#8f7a5a)" role="img" aria-label="Photo of a carer playing with dogs in an outdoor pen"></div>
<div class="abs card" style="left:780px;background:linear-gradient(160deg,#eef0ee,#d4a46a 50%,#5a6a8a)" role="img" aria-label="Photo of a woman greeting a golden retriever indoors"></div>
<div class="abs card-label" style="left:111px">We Feed</div>
<div class="abs card-label" style="left:446px">Walk And Play With Your Pet</div>
<div class="abs card-label" style="left:780px">Each Visit</div>

<!-- costs -->
<h2 class="abs sec-title script" style="left:114px;top:2196px">Costs</h2>
<p class="abs copy" style="left:111px;top:2271px;width:485px">Lorem ipsum dolor sit amet, consectetur adipiscing elit, sed do eiusmod tempor incididunt ut labore et dolore magna aliqua. Ut enim ad minim veniam, quis nostrud exercitation laboris nisi ut aliquip ex ea commodo consequat. Duis aute irure dolor in reprehenderit in voluptate velit esse cillum dolore eu fugiat nulla pariatur. Excepteur sint occaecat cupidatat non proident, sunt in culpa qui officia deserunt mollit anim id est laborum</p>
<p class="abs copy" style="left:111px;top:2410px;width:485px">Lorem ipsum dolor sit amet, consectetur adipiscing elit, sed do eiusmod tempor incididunt ut labore et dolore magna aliqua. Ut enim ad minim veniam, quis nostrud exercitation laboris nisi ut aliquip ex ea commodo consequat. Duis aute irure dolor in reprehenderit in voluptate velit esse cillum dolore eu fugiat nulla pariatur. Excepteur sint occaecat cupidatat non proident, sunt in culpa qui officia deserunt mollit anim id est laborum</p>
<a class="btn" style="left:111px;top:2567px">Read More</a>
<div class="abs arch" style="left:658px;top:2136px;width:428px;height:507px;background:linear-gradient(180deg,#6a7a4a 0%,#9a5a2a 40%,#7a3a1a 80%,#4a4a4a 100%)" role="img" aria-label="Photo of a red-coated dog standing on a rock outdoors"></div>
<div class="abs badge"><div>$8/<small>per</small> Visit</div><div>2 Visits a Day</div></div>

<!-- contact -->
<div class="abs contact" role="img" aria-label="Photo of a woman hugging her dog at home"></div>
<div class="abs contact-shade"></div>
<h2 class="abs script" style="left:0;width:1200px;text-align:center;top:2834px;font-size:44px;color:var(--white)">Contact Us</h2>
<div class="abs field" style="left:117px;top:2919px;width:474px;height:55px">Name</div>
<div class="abs field" style="left:606px;top:2919px;width:471px;height:55px">Email</div>
<div class="abs field" style="left:117px;top:2988px;width:474px;height:57px">Phone Number</div>
<div class="abs field" style="left:606px;top:2988px;width:471px;height:57px;justify-content:space-between">Services
  <svg width="10" height="6" viewBox="0 0 10 6"><path d="M0 0h10L5 6z" fill="#fff"/></svg></div>
<div class="abs field" style="left:117px;top:3056px;width:960px;height:137px;align-items:flex-start;padding-top:18px">Message</div>
<a class="btn" style="left:480px;top:3220px;width:240px">Submit Now</a>

<!-- footer -->
<footer class="abs footer"></footer>
<div class="abs f-head" style="left:109px;color:var(--white)">QUICK LINKS</div>
<div class="abs f-head" style="left:276px;color:var(--white)">SERVICES</div>
<div class="abs f-head" style="left:505px;color:var(--white)">CONTACT US</div>
<div class="abs f-head" style="left:813px;color:var(--white)">NEWSLETTER</div>
<div class="abs f-rule" style="left:109px"></div>
<div class="abs f-rule" style="left:276px"></div>
<div class="abs f-rule" style="left:505px"></div>
<div class="abs f-rule" style="left:813px"></div>
<div class="abs f-list" style="left:109px;color:var(--white)">Home<br>About Us<br>Costs<br>Services<br>Contact</div>
<div class="abs f-list" style="left:276px;color:var(--white);line-height:34px;top:3486px">We Feed<br>Walk And Play With Your Pet<br>Each Visit</div>
<div class="abs" style="left:505px;top:3492px;color:var(--white);font-size:13px;line-height:20px">
  <div class="f-small">ADDRESS</div>
  <div style="display:flex;gap:6px;align-items:center"><svg width="10" height="13" viewBox="0 0 10 13"><path d="M5 0a5 5 0 0 0-5 5c0 4 5 8 5 8s5-4 5-8a5 5 0 0 0-5-5zm0 7a2 2 0 1 1 0-4 2 2 0 0 1 0 4z" fill="#fff"/></svg>Lorem ipsum dolor sit amet</div>
  <div class="f-small" style="margin-top:16px">PHONE</div>
  <div style="display:flex;gap:6px;align-items:center"><svg width="12" height="12" viewBox="0 0 12 12"><path d="M2.5 0 4.5 2.5 3.3 4a7 7 0 0 0 4.7 4.7L9.5 7.5 12 9.5 10.5 12C5 12 0 7 0 1.5z" fill="#fff"/></svg>+1 888 888 8888</div>
  <div class="f-small" style="margin-top:16px">EMAIL</div>
  <div style="display:flex;gap:6px;align-items:center"><svg width="13" height="10" viewBox="0 0 13 10"><rect width="13" height="10" rx="1" fill="#fff"/><path d="M0 1l6.5 4.5L13 1" fill="none" stroke="#ee7325" stroke-width="1.3"/></svg>hello@pawspalspetcare.com</div>
</div>
<p class="abs" style="left:813px;top:3490px;width:270px;font-size:13px;line-height:23px;color:var(--white)">Lorem ipsum dolor sit amet, consectetur adipiscing elit, sed do eiusmod tempor</p>
<div class="abs" style="left:810px;top:3563px;width:276px;height:38px;border-radius:20px;background:var(--white);display:flex;align-items:center;justify-content:space-between;padding:0 14px 0 20px;font-size:13px;color:#333">Enter Email
  <svg width="18" height="18" viewBox="0 0 18 18"><circle cx="9" cy="9" r="9" fill="#ee7325"/><path d="M4 9l10-4-3 9-2-3z" fill="#fff"/></svg></div>
<div class="abs social" style="left:817px">Net</div>
<div class="abs social" style="left:870px">Pix</div>
<div class="abs social" style="left:925px">Pal</div>
<div class="abs" style="left:109px;top:3707px;width:980px;height:1px;background:rgba(255,255,255,.6)"></div>
<div class="abs" style="left:0;width:1200px;text-align:center;top:3739px;font-size:14px;color:var(--white)">&copy; 2022. All Rights Reserved</div>

</body>
</html>
```